Package design for quilted mattress covers.

We are producing a comfortable "quilted mattress protector" for beds . We need a very elegant and attractive and cozy insert label. approx. size is 14 inches high x11 inches wide. (One base design with slight edits to customize for each different bed size) It will be packaged in a nice clear bag, with the design label in front. I attached the type of product for reference

package text:
QUILTED MATTRESS COVER

size: 33x75x10"

*ultimate comfort
*breathable cotton top
*waterproof lining
*easy care wash and dry
Updates

Target Market(s)

displayed in drygood and bedding retail stores

Colors

Designer to choose colors to be used in the design.

Requirements
Must have
• all info as in description
Nice to have
• an image of a quilted cover on a bed, professionally included in the package design
Should not have
• ..

```html
<!DOCTYPE html>
<html lang="en">
<head>
<meta charset="utf-8">
<title>Lumora Quilted Mattress Cover Label</title>
<link rel="stylesheet" href="https://fonts.googleapis.com/css2?family=Inter:wght@200;300;400;500;600&display=swap">
<style>
  :root {
    --navy: #3a5a8e;
    --navy-soft: rgba(74, 110, 176, 0.45);
    --white: #ffffff;
    --title-grey: #9c9ca0;
    --band-light: #a5a5a9;
    --band-dark: #8f8f94;
    --icon-fill: #a8d4f6;
    --icon-line: #1d2a44;
    --wall: #b3c3d4;
    --wall-light: #c6d2de;
    --window: #f2eddf;
    --linen: #f7f7f5;
    --frame: #cbc3b5;
    --floor: #b6a993;
  }
  * { margin: 0; padding: 0; box-sizing: border-box; }
  html, body { width: 944px; height: 1200px; overflow: hidden; background: var(--white); }
  .label {
    position: relative;
    width: 944px;
    height: 1200px;
    overflow: hidden;
    font-family: "Inter", Arial, sans-serif;
    font-feature-settings: "calt" 0;
  }
  .hero-photo {
    position: absolute;
    left: 0; top: 0;
    width: 944px; height: 965px;
    background:
      radial-gradient(ellipse 220px 380px at 790px 330px, rgba(242,237,223,0.95) 0%, rgba(242,237,223,0.6) 55%, rgba(242,237,223,0) 100%),
      radial-gradient(ellipse 430px 150px at 510px 520px, var(--linen) 0%, rgba(247,247,245,0.95) 60%, rgba(247,247,245,0) 100%),
      radial-gradient(ellipse 160px 90px at 310px 360px, rgba(214,207,195,0.9) 0%, rgba(214,207,195,0) 100%),
      radial-gradient(ellipse 420px 110px at 520px 700px, rgba(203,195,181,0.9) 0%, rgba(203,195,181,0) 100%),
      linear-gradient(180deg, var(--wall) 0%, var(--wall-light) 30%, #d6d4cf 48%, #d2cbbf 62%, #c6bca9 76%, var(--floor) 100%);
  }
  .chevrons { position: absolute; left: 0; top: 0; width: 944px; height: 965px; }
  .brand {
    position: absolute;
    left: 560px; top: 122px;
    width: 330px;
    text-align: center;
    font-weight: 600;
    font-size: 66px;
    line-height: 1;
    letter-spacing: -1.5px;
    color: var(--navy);
  }
  .title {
    position: absolute;
    color: var(--title-grey);
    font-weight: 200;
    font-size: 60px;
    line-height: 1;
    letter-spacing: 1.5px;
    white-space: nowrap;
  }
  .title-line-1 { top: 786px; left: 575px; }
  .title-line-2 { top: 860px; right: 56px; }
  .size-tag {
    position: absolute;
    left: 0; top: 910px;
    width: 340px; height: 55px;
  }
  .size-tag svg { position: absolute; inset: 0; }
  .size-text {
    position: absolute;
    left: 38px; top: 11px;
    color: var(--white);
    font-weight: 500;
    font-size: 27px;
    white-space: nowrap;
  }
  .features {
    position: absolute;
    left: 0; top: 965px;
    width: 944px; height: 167px;
    background: linear-gradient(180deg, var(--band-light) 0 100px, var(--band-dark) 100px 167px);
    display: flex;
  }
  .feature {
    flex: 1;
    display: flex;
    flex-direction: column;
    align-items: center;
  }
  .feature-icon { margin-top: 20px; width: 62px; height: 64px; }
  .feature-label {
    margin-top: 30px;
    color: var(--white);
    font-weight: 300;
    font-size: 17.5px;
    line-height: 22px;
    text-align: center;
  }
  .footer-band {
    position: absolute;
    left: 0; top: 1136px;
    width: 944px; height: 64px;
    background: var(--navy);
  }
</style>
</head>
<body>
<main class="label">
  <div class="hero-photo" role="img" aria-label="Photo of a bed in a bright bedroom with pale blue walls and a curtained window, made up with a white quilted mattress cover, white pillows and a navy cushion, on a beige rug"></div>

  <svg class="chevrons" viewBox="0 0 944 965" aria-hidden="true">
    <polygon points="150,965 679,598 944,750 944,965" fill="var(--navy-soft)" opacity="0.5"/>
    <polygon points="190,965 679,630 944,790 944,965" fill="var(--navy-soft)" opacity="0.7"/>
    <polygon points="222,965 679,655 944,808 944,965" fill="var(--navy-soft)"/>
    <polygon points="242,965 679,677 944,818 944,965" fill="var(--white)"/>
  </svg>

  <div class="brand">Lumora</div>

  <div class="title title-line-1">Quilted</div>
  <div class="title title-line-2">Mattress Cover</div>

  <div class="size-tag">
    <svg viewBox="0 0 340 55" aria-hidden="true"><polygon points="0,0 298,0 340,55 0,55" fill="var(--navy)"/></svg>
    <span class="size-text">Size: 33 x 75 x 10"</span>
  </div>

  <section class="features">
    <div class="feature">
      <svg class="feature-icon" viewBox="0 0 62 64" aria-hidden="true">
        <rect x="2" y="20" width="58" height="42" rx="2" fill="var(--icon-fill)" stroke="var(--icon-line)" stroke-width="2.5"/>
        <rect x="10" y="2" width="42" height="26" rx="3" fill="var(--white)" stroke="var(--icon-line)" stroke-width="2.5"/>
        <line x1="18" y1="40" x2="18" y2="56" stroke="var(--icon-line)" stroke-width="2.5"/>
        <line x1="44" y1="40" x2="44" y2="56" stroke="var(--icon-line)" stroke-width="2.5"/>
      </svg>
      <div class="feature-label">Ultimate<br>Comfort</div>
    </div>
    <div class="feature">
      <svg class="feature-icon" viewBox="0 0 62 64" aria-hidden="true">
        <circle cx="16" cy="14" r="10" fill="var(--icon-fill)" stroke="var(--icon-line)" stroke-width="2.5"/>
        <rect x="2" y="34" width="58" height="16" rx="3" fill="var(--icon-fill)" stroke="var(--icon-line)" stroke-width="2.5"/>
        <rect x="6" y="26" width="18" height="10" rx="3" fill="var(--white)" stroke="var(--icon-line)" stroke-width="2.5"/>
        <line x1="8" y1="50" x2="8" y2="60" stroke="var(--icon-line)" stroke-width="3"/>
        <line x1="54" y1="50" x2="54" y2="60" stroke="var(--icon-line)" stroke-width="3"/>
        <line x1="2" y1="60" x2="60" y2="60" stroke="var(--icon-line)" stroke-width="2.5"/>
      </svg>
      <div class="feature-label">Breathable<br>Cotton Top</div>
    </div>
    <div class="feature">
      <svg class="feature-icon" viewBox="0 0 62 64" aria-hidden="true">
        <path d="M14 6 C10 13 7 16 7 20 a7 7 0 0 0 14 0 C21 16 18 13 14 6Z" fill="var(--icon-fill)" stroke="var(--icon-line)" stroke-width="2.5"/>
        <path d="M40 2 C34 12 29 17 29 23 a11 11 0 0 0 22 0 C51 17 46 12 40 2Z" fill="var(--icon-fill)" stroke="var(--icon-line)" stroke-width="2.5"/>
        <rect x="4" y="44" width="56" height="10" fill="var(--white)" stroke="var(--icon-line)" stroke-width="2.5"/>
        <line x1="4" y1="38" x2="4" y2="62" stroke="var(--icon-line)" stroke-width="3"/>
        <line x1="60" y1="46" x2="60" y2="62" stroke="var(--icon-line)" stroke-width="3"/>
        <rect x="8" y="38" width="14" height="6" rx="2" fill="var(--icon-fill)" stroke="var(--icon-line)" stroke-width="2"/>
      </svg>
      <div class="feature-label">Waterproof<br>Lining</div>
    </div>
    <div class="feature">
      <svg class="feature-icon" viewBox="0 0 62 64" aria-hidden="true">
        <rect x="6" y="2" width="50" height="60" rx="2" fill="var(--icon-fill)" stroke="var(--icon-line)" stroke-width="2.5"/>
        <line x1="6" y1="14" x2="56" y2="14" stroke="var(--icon-line)" stroke-width="2.5"/>
        <circle cx="44" cy="8" r="2.5" fill="var(--icon-line)"/>
        <circle cx="31" cy="38" r="15" fill="var(--white)" stroke="var(--icon-line)" stroke-width="2.5"/>
        <circle cx="31" cy="38" r="8" fill="var(--icon-fill)" stroke="var(--icon-line)" stroke-width="2.5"/>
      </svg>
      <div class="feature-label">Easy Care<br>Wash &amp; Dry</div>
    </div>
  </section>

  <div class="footer-band"></div>
</main>
</body>
</html>
```